New Zealand Marlborough Sauvignon Blanc wine packaging design

We need packaging design for our new wine brand, Dunmore Hale. The wine is a New Zealand Marlborough Sauvignon Blanc. We would like the packaging will portray elegance and style with an understated label. We are looking for a label that portrays the elegance of the French Riviera. The label should be round or pill shaped.
Updates

Industry/Entity Type

Wine

Font styles to use
Serif
Sans Serif

Requirements
Must have
• The words in order of importance: Dunmore Hale, Sauvignon Blanc, Marlborough, New Zealand. It should be fit to the bottle posted in the links
Nice to have
• a pill shape or circular shape
Should not have
• Illustrations of wine bottles, wine glasses, or grapes

```html
<!DOCTYPE html>
<html lang="en">
<head>
<meta charset="utf-8">
<title>Dunmore Hale — Marlborough Sauvignon Blanc Label</title>
<link href="https://fonts.googleapis.com/css2?family=Graduate&family=Libre+Baskerville:wght@700&family=Special+Elite&display=swap" rel="stylesheet">
<style>
  :root {
    --backdrop: #f58a1f;
    --label-cream: #fdf6ee;
    --label-cream-edge: #f6e9dc;
    --ink: #0d0d0d;
    --band-text: #ffffff;
    --scene-light: #c9c7c1;
    --scene-dark: #5b5a55;
  }
  html, body {
    margin: 0;
    padding: 0;
    width: 846px;
    height: 1200px;
    overflow: hidden;
    background: var(--backdrop);
  }
  .canvas {
    position: relative;
    width: 846px;
    height: 1200px;
  }
  .label {
    position: absolute;
    left: 113px;
    top: 160px;
    width: 620px;
    height: 880px;
    border-radius: 50% / 38%;
    background: radial-gradient(ellipse at 50% 40%, var(--label-cream) 60%, var(--label-cream-edge) 100%);
    box-shadow: 0 4px 14px rgba(0,0,0,0.18);
  }
  .label-frame {
    position: absolute;
    inset: 14px;
    border: 3px solid var(--ink);
    border-radius: 50% / 38%;
  }
  .label-art {
    position: absolute;
    left: 50%;
    top: 82px;
    width: 320px;
    height: 210px;
    transform: translateX(-50%);
    background: linear-gradient(180deg, var(--scene-light) 0%, #e6e3dc 40%, var(--scene-dark) 100%);
    opacity: 0.75;
  }
  .label-category {
    position: absolute;
    top: 330px;
    width: 100%;
    text-align: center;
    font-family: "Libre Baskerville", Georgia, serif;
    font-weight: 700;
    font-size: 33px;
    letter-spacing: 7px;
    color: var(--ink);
  }
  .label-band {
    position: absolute;
    top: 398px;
    left: 14px;
    right: 14px;
    height: 84px;
    background: var(--ink);
    display: flex;
    align-items: center;
    justify-content: center;
  }
  .brand-name {
    font-family: "Graduate", "Courier New", serif;
    font-size: 58px;
    letter-spacing: 2px;
    color: var(--band-text);
    white-space: nowrap;
  }
  .varietal {
    position: absolute;
    top: 502px;
    width: 100%;
    text-align: center;
    font-family: "Special Elite", "Courier New", monospace;
    font-size: 36px;
    line-height: 48px;
    color: var(--ink);
    -webkit-text-stroke: 0.8px var(--ink);
  }
  .spec-row {
    position: absolute;
    top: 668px;
    left: 50%;
    transform: translateX(-50%);
    width: 360px;
    height: 50px;
    border-top: 2px solid var(--ink);
    border-bottom: 2px solid var(--ink);
    display: flex;
    align-items: center;
    justify-content: space-between;
    font-family: "Libre Baskerville", Georgia, serif;
    font-size: 22px;
    letter-spacing: 8px;
    color: var(--ink);
  }
  .spec-dot {
    width: 14px;
    height: 14px;
    border-radius: 50%;
    background: var(--ink);
    margin: 0 4px;
  }
  .label-stars {
    position: absolute;
    top: 752px;
    left: 50%;
    transform: translateX(-50%);
  }
</style>
</head>
<body>
  <main class="canvas">
    <section class="label">
      <div class="label-frame"></div>
      <div class="label-art" role="img" aria-label="Pen sketch of a Riviera seaside town with rooftops, church towers and a curving bay"></div>
      <div class="label-category">WHITE WINE</div>
      <div class="label-band"><h1 class="brand-name" style="margin:0;font-weight:400;">DUNMORE HALE</h1></div>
      <div class="varietal">New Zealand Marlborough<br>Sauvignon Blanc</div>
      <div class="spec-row">
        <span class="spec-dot"></span>
        <span class="spec-text">750mL&nbsp;&nbsp;43%Alc</span>
        <span class="spec-dot"></span>
      </div>
      <svg class="label-stars" width="120" height="50" viewBox="0 0 120 50" aria-hidden="true">
        <g fill="#0d0d0d">
          <polygon points="15,18 19,28 30,28 21,34 24,45 15,38 6,45 9,34 0,28 11,28"/>
          <polygon points="60,3 64,13 75,13 66,19 69,30 60,23 51,30 54,19 45,13 56,13"/>
          <polygon points="105,18 109,28 120,28 111,34 114,45 105,38 96,45 99,34 90,28 101,28"/>
        </g>
      </svg>
    </section>
  </main>
</body>
</html>
```